Harvest Poster

I need a poster for a television show. The poster would be used primarily online and I want it to be rectangle to mirror 16:9 TV aspect ratio. The name of the program is “Harvest” (logo attached). “Harvest” will be a 30 minute weekly show that features interviews from all walks of life of how the transforming power of God has changed lives. I want the logo to be included on the poster, and little section left open so I can add pictures of people that will share their story for each episode. The text should also include “Bellwick tv” logo (TV station producing show), name of producer and where the show can be viewed.
Tv

```html
<!DOCTYPE html>
<html lang="en">
<head>
<meta charset="utf-8">
<title>Harvest Poster</title>
<link rel="stylesheet" href="https://fonts.googleapis.com/css2?family=Exo+2:wght@200;300;600&display=swap">
<style>
  :root {
    --page: #ffffff;
    --night: #050506;
    --night-soft: #121316;
    --teal-glow: rgba(60, 110, 130, 0.55);
    --rose-glow: rgba(150, 90, 90, 0.35);
    --mist: rgba(200, 200, 205, 0.16);
    --title: #d9d9dc;
    --brand: #ffffff;
    --credit: #a9a9ae;
  }
  * { margin: 0; padding: 0; box-sizing: border-box; }
  html, body {
    width: 1200px;
    height: 900px;
    overflow: hidden;
    background: var(--page);
  }
  .poster {
    position: absolute;
    left: 103px;
    top: 168px;
    width: 994px;
    height: 559px;
    overflow: hidden;
    background:
      radial-gradient(circle at 78% 38%, var(--mist) 0, transparent 18%),
      radial-gradient(circle at 92% 62%, var(--mist) 0, transparent 12%),
      radial-gradient(circle at 58% 78%, rgba(200,200,205,0.10) 0, transparent 10%),
      linear-gradient(90deg, var(--night-soft) 0%, var(--night) 60%, #0a0a0c 100%);
  }
  .guest-photo {
    position: absolute;
    left: 0;
    top: 0;
    width: 560px;
    height: 559px;
    background:
      radial-gradient(ellipse 45% 30% at 50% 14%, rgba(140,140,140,0.9) 0, transparent 100%),
      radial-gradient(ellipse 40% 45% at 50% 48%, rgba(185,170,160,0.85) 0, transparent 100%),
      radial-gradient(ellipse 60% 50% at 20% 40%, var(--teal-glow) 0, transparent 100%),
      radial-gradient(ellipse 40% 40% at 70% 20%, var(--rose-glow) 0, transparent 100%),
      radial-gradient(ellipse 55% 30% at 40% 92%, rgba(110,110,110,0.8) 0, transparent 100%),
      linear-gradient(90deg, rgba(20,30,40,0.9) 0%, rgba(5,5,6,0) 100%);
  }
  .show-title {
    position: absolute;
    left: 396px;
    top: 334px;
    width: 540px;
    display: flex;
    justify-content: space-between;
    font-family: "Exo 2", sans-serif;
    font-weight: 200;
    font-size: 32px;
    line-height: 1;
    color: var(--title);
  }
  .station {
    position: absolute;
    right: 56px;
    top: 438px;
    display: flex;
    align-items: center;
    gap: 6px;
    font-family: "Exo 2", sans-serif;
    font-weight: 600;
    font-size: 21px;
    line-height: 1;
    color: var(--brand);
  }
  .station-mark {
    width: 14px;
    height: 14px;
    background: var(--brand);
  }
  .credits {
    position: absolute;
    right: 56px;
    top: 478px;
    text-align: right;
    font-family: "Exo 2", sans-serif;
    font-weight: 300;
    font-size: 13px;
    line-height: 1.5;
    letter-spacing: 0.04em;
    color: var(--credit);
  }
</style>
</head>
<body>
  <main class="poster">
    <div class="guest-photo" role="img" aria-label="Portrait of a smiling grey-haired guest in a fleece jacket against soft blue bokeh lights"></div>
    <h1 class="show-title" aria-label="Harvest">
      <span>H</span><span>A</span><span>R</span><span>V</span><span>E</span><span>S</span><span>T</span>
    </h1>
    <div class="station">
      <span>Bellwick tv</span>
      <span class="station-mark"></span>
    </div>
    <div class="credits">
      <p class="producer">Produced by Mara Ellison</p>
      <p class="viewing">Watch weekly at bellwick.tv</p>
    </div>
  </main>
</body>
</html>
```